Redesign Charity Golf Outing Flyer

We need a redesign of our current golf outing flyer. The charity is in the name of a fallen police officer and the funds help scholarships for future police officers and community projects. I have included the artwork from last year. We brand everything with "The Chief 417" because Derek's badge number was 417 and he often told people he was "The Chief". The details on the flyer will need to be editable (we have access to the full Adobe creative suite). While the cause is serious the event itself is fun so feel free to have fun with it.

Target Market(s)

Golfers and people who want to donate.

Industry/Entity Type

Charity

Font styles to use
Sans Serif

Colors
0555a3

Requirements
Must have
• All information included on last years flyer.
Nice to have
• A modern feel.
Should not have
• N/a

```html
<!DOCTYPE html>
<html lang="en">
<head>
<meta charset="utf-8">
<title>Remembering The Chief – Memorial &amp; Scholarship Golf Scramble</title>
<link rel="stylesheet" href="https://fonts.googleapis.com/css2?family=Arimo:wght@400;700&family=Oswald:wght@500&family=Roboto+Condensed:wght@500&family=Open+Sans:wght@400;600;700&display=swap">
<style>
  :root {
    --brand-blue: #0555a3;
    --ink: #3a3a3a;
    --ink-dark: #222;
    --paper: #ffffff;
    --line: #333;
    --sky-dark: #2a1a0c;
    --sky-warm: #b8621c;
    --grass: #5f7d22;
    --grass-light: #a9b94a;
  }
  * { margin: 0; padding: 0; box-sizing: border-box; }
  html, body { width: 923px; height: 1200px; overflow: hidden; background: var(--paper); }
  .flyer { position: relative; width: 923px; height: 1200px; background: var(--paper); font-family: "Open Sans", sans-serif; color: var(--ink-dark); }
  .abs { position: absolute; }

  .hero-photo { left: 0; top: 0; width: 923px; height: 400px;
    background: linear-gradient(180deg, var(--sky-dark) 0%, var(--sky-warm) 20%, #6b5a25 38%, var(--grass) 58%, var(--grass-light) 80%, var(--grass) 100%); }
  .hero-curves { left: 0; top: 0; }
  .hero-title { left: 60px; top: 46px; font-family: "Arimo", sans-serif; font-weight: 700; font-size: 69px; line-height: 62px; color: #fff; letter-spacing: 1px; }
  .event-brand { left: 604px; top: 158px; width: 180px; text-align: center; font-family: "Arimo", sans-serif; font-weight: 700; font-size: 22px; color: var(--paper); }

  .portrait-ring { left: 100px; top: 177px; width: 299px; height: 299px; border-radius: 50%; background: var(--brand-blue); }
  .portrait { left: 110px; top: 187px; width: 279px; height: 279px; border-radius: 50%;
    background: linear-gradient(180deg, #f0f0f0 0%, #d8d8d8 50%, #3a4050 75%, #1c2233 100%); }

  .side-rule { width: 2px; background: var(--brand-blue); }

  .event-name { left: 55px; top: 490px; }
  .event-name .edition { font-family: "Oswald", sans-serif; font-weight: 500; font-size: 34px; line-height: 38px; color: var(--brand-blue); }
  .event-name .kind { font-family: "Roboto Condensed", sans-serif; font-weight: 500; font-size: 46px; line-height: 46px; color: var(--ink); }
  .event-name .format { font-family: "Arimo", sans-serif; font-weight: 700; font-size: 50px; line-height: 50px; color: var(--brand-blue); }

  .date-box { left: 506px; top: 484px; width: 402px; height: 132px; background: var(--brand-blue); color: #fff; text-align: right; padding: 8px 16px 0 0; }
  .date-box .date { font-family: "Oswald", sans-serif; font-weight: 500; font-size: 34px; line-height: 38px; }
  .date-box .time { font-family: "Arimo", sans-serif; font-size: 27px; line-height: 30px; }
  .date-box .time small { font-size: 21px; }
  .date-box .note { font-size: 18.5px; line-height: 22px; }

  .fee { left: 52px; top: 646px; }
  .fee .label { font-family: "Arimo", sans-serif; font-weight: 700; font-size: 47px; letter-spacing: 4px; color: var(--ink); line-height: 54px; }
  .fee .price { font-family: "Oswald", sans-serif; font-weight: 500; font-size: 40px; color: var(--brand-blue); line-height: 48px; }
  .fee .price small { font-size: 27px; }
  .fee .includes { font-size: 23.5px; color: var(--ink); line-height: 28px; margin-top: -6px; }

  .venue { right: 30px; top: 637px; text-align: right; font-size: 15.5px; line-height: 21.5px; color: var(--ink-dark); }
  .venue .venue-name, .venue .url { font-weight: 700; color: var(--brand-blue); }
  .venue .register { margin-top: 16px; }

  .divider { left: 16px; top: 808px; width: 877px; height: 5px; background: var(--brand-blue); }

  .section-title { font-family: "Open Sans", sans-serif; font-weight: 700; color: var(--brand-blue); }
  .captain { left: 55px; top: 834px; width: 400px; }
  .captain .section-title { font-size: 18px; margin-bottom: 8px; }
  .field { display: flex; align-items: flex-end; font-size: 14.5px; height: 28.3px; color: var(--ink-dark); }
  .field .blank { flex: 1; border-bottom: 1px solid var(--line); margin-left: 4px; height: 16px; }
  .field .blank.city { flex: 0 0 155px; margin-right: 4px; }
  .field .blank.state { flex: 0 0 50px; margin-right: 0; }
  .mail-info { margin-top: 12px; font-size: 14px; line-height: 18px; }

  .mail-bar { left: 0; top: 1166px; width: 464px; height: 34px; background: var(--brand-blue); color: #fff; font-weight: 700; font-size: 17px; line-height: 34px; padding-left: 54px; }
  .connector { left: 0; top: 0; }

  .sponsor { left: 514px; top: 834px; width: 390px; }
  .sponsor .section-title { font-size: 23.5px; line-height: 25px; }
  .sponsor .ask { margin-top: 12px; font-size: 14.5px; }
  .sponsor .line-only { width: 278px; border-bottom: 1px solid var(--line); height: 20px; }
  .sponsor .field { margin-top: 14px; }
  .sponsor .field .blank { flex: 0 0 174px; }

  .contact-box { left: 529px; top: 998px; width: 300px; height: 125px; background: var(--brand-blue); color: #fff; text-align: center; font-size: 15px; line-height: 20px; padding-top: 14px; font-style: normal; }
  .contact-box strong { font-weight: 700; font-size: 16px; }
</style>
</head>
<body>
<main class="flyer">
  <div class="abs hero-photo" role="img" aria-label="Photo of a golf ball on a tee on a fairway at sunset"></div>

  <svg class="abs hero-curves" width="923" height="480" viewBox="0 0 923 480" aria-hidden="true">
    <path d="M0 255 C 180 330, 300 390, 420 400 C 620 410, 800 350, 923 295 L923 480 L0 480 Z" fill="var(--brand-blue)"/>
    <path d="M0 330 C 190 395, 320 420, 440 425 C 640 430, 810 380, 923 312 L923 480 L0 480 Z" fill="var(--paper)"/>
  </svg>

  <h1 class="abs hero-title">REMEMBERING<br>"THE CHIEF"</h1>
  <div class="abs event-brand">The Chief 417</div>

  <div class="abs portrait-ring"></div>
  <div class="abs portrait" role="img" aria-label="Portrait of Officer Derek D. Halloran in uniform"></div>

  <div class="abs side-rule" style="left:16px; top:331px; height:479px;"></div>
  <div class="abs side-rule" style="left:906px; top:305px; height:505px;"></div>

  <div class="abs event-name">
    <div class="edition">2ND ANNUAL DEREK D. HALLORAN</div>
    <div class="kind">Memorial &amp; Scholarship</div>
    <div class="format">GOLF SCRAMBLE</div>
  </div>

  <div class="abs date-box">
    <div class="date">SATURDAY-AUGUST 15, 2015</div>
    <div class="time">9<small>am</small> Registration</div>
    <div class="note">Day of scramble registrations are welcome</div>
    <div class="time">10<small>am</small> Shotgun Start</div>
  </div>

  <div class="abs fee">
    <div class="label">ENTRY FEE</div>
    <div class="price">$55/PERSON <small>($220/TEAM)</small></div>
    <div class="includes">Includes: Green fees, cart and dinner</div>
  </div>

  <address class="abs venue" style="font-style:normal;">
    <div class="venue-name">Cedar Ridge Golf Course</div>
    <div>4810 Birchwood Valley Rd.</div>
    <div>Millbrook, OH 44990</div>
    <div>(555) 314-2681</div>
    <div class="register">Register below or online at:</div>
    <div class="url">www.417golf.example.org</div>
  </address>

  <div class="abs divider"></div>

  <section class="abs captain">
    <h2 class="section-title">TEAM CAPTIAN INFORMATION:</h2>
    <div class="field">Captain’s Name:<span class="blank"></span></div>
    <div class="field">Address:<span class="blank"></span></div>
    <div class="field">City:<span class="blank city"></span>State:<span class="blank state"></span>Zip:<span class="blank"></span></div>
    <div class="field">Captain’s Phone:<span class="blank"></span></div>
    <div class="field">Captain’s Email:<span class="blank"></span></div>
    <div class="field">Player # 2 Name:<span class="blank"></span></div>
    <div class="field">Player # 3 Name:<span class="blank"></span></div>
    <div class="field">Player # 4 Name:<span class="blank"></span></div>
    <p class="mail-info"><strong>Mail-in Deadline: August 1, 2015</strong><br>
      Mail this completed form with check(s) made payable to:<br>
      “The Officer Derek D. Halloran Memorial Scholarship Fund”</p>
  </section>

  <div class="abs mail-bar">Mail to contact information on the right.</div>

  <svg class="abs connector" width="923" height="1200" viewBox="0 0 923 1200" aria-hidden="true">
    <path d="M464 1183 H715 V1136" stroke="var(--line)" stroke-width="1.5" fill="none"/>
    <path d="M709 1138 L715 1128 L721 1138 Z" fill="var(--line)"/>
  </svg>

  <section class="abs sponsor">
    <h2 class="section-title">Can’t Make it or Don’t Golf?<br>Sponsor a hole/tee:</h2>
    <p class="ask">Name/Bussiness (attach bussiness card if possible):</p>
    <div class="line-only"></div>
    <div class="field">Donation Amont:<span class="blank"></span></div>
  </section>

  <address class="abs contact-box">
    <strong>Any Questions Contact:</strong><br>
    Gordon Whitley<br>
    2735 Maple Crest Lane<br>
    Fairhaven, OH 44991<br>
    (555) 208-7749
  </address>
</main>
</body>
</html>
```